Business Cards

We are an innovating group of real estate investors who buy beat up house's, fix them up, and resell them. We are in need of a business card that is catchy and stands out. We want it to say something like " We buy house's cash fast" Call us first

Industry/Entity Type

Business

Requirements
Must have
• Our logo which is updated

```html
<!DOCTYPE html>
<html lang="en">
<head>
<meta charset="utf-8">
<title>Bayline Homes – Business Card</title>
<link href="https://fonts.googleapis.com/css2?family=Source+Sans+3:wght@400;600&family=Architects+Daughter&display=swap" rel="stylesheet">
<style>
  :root {
    --page: #ffffff;
    --card: #000000;
    --band-gray: #3b3b3b;
    --purple: #b0409b;
    --purple-bright: #c04aa8;
    --purple-deep: #581a54;
    --silver-light: #f2f2f2;
    --silver-dark: #8a8a8a;
    --text-light: #ffffff;
    --tagline: #d0d0d0;
  }
  html, body {
    margin: 0;
    padding: 0;
    width: 1074px;
    height: 1200px;
    overflow: hidden;
    background: var(--page);
  }
  .canvas {
    position: relative;
    width: 1074px;
    height: 1200px;
    font-family: "Source Sans 3", "Helvetica Neue", Arial, sans-serif;
  }
  .card {
    position: absolute;
    left: 66px;
    width: 936px;
    background: var(--card);
    overflow: hidden;
  }
  .card--front { top: 43px; height: 507px; }
  .card--back { top: 606px; height: 534px; }
  .card__art {
    position: absolute;
    inset: 0;
    width: 100%;
    height: 100%;
  }
  .brand {
    position: absolute;
    display: flex;
    align-items: center;
    gap: 12px;
    transform: translate(-50%, -50%);
    color: var(--purple-bright);
    font-weight: 600;
    white-space: nowrap;
  }
  .brand__square {
    background: var(--purple-bright);
    flex: none;
  }
  .card--front .brand { left: 224px; top: 244px; font-size: 32px; }
  .card--front .brand__square { width: 22px; height: 22px; }
  .card--back .brand { left: 468px; top: 177px; font-size: 50px; gap: 16px; }
  .card--back .brand__square { width: 34px; height: 34px; }
  .contact__name {
    position: absolute;
    left: 483px;
    top: 112px;
    margin: 0;
    font-size: 46px;
    font-weight: 400;
    color: var(--text-light);
    letter-spacing: 0.5px;
  }
  .contact__title {
    position: absolute;
    left: 545px;
    top: 182px;
    margin: 0;
    font-size: 27px;
    color: var(--purple);
  }
  .contact__email {
    position: absolute;
    left: 483px;
    top: 230px;
    margin: 0;
    font-size: 24px;
    color: var(--text-light);
  }
  .contact__phone {
    position: absolute;
    right: 68px;
    top: 400px;
    margin: 0;
    font-size: 40px;
    color: var(--text-light);
  }
  .tagline {
    position: absolute;
    left: 0;
    right: 0;
    top: 362px;
    margin: 0;
    text-align: center;
    font-family: "Architects Daughter", "Comic Sans MS", cursive;
    font-size: 26px;
    letter-spacing: 2px;
    color: var(--tagline);
  }
</style>
</head>
<body>
<main class="canvas">

  <section class="card card--front" aria-label="Card front">
    <svg class="card__art" viewBox="0 0 936 507" aria-hidden="true">
      <defs>
        <linearGradient id="silver-v" x1="0" y1="0" x2="1" y2="0">
          <stop offset="0" stop-color="var(--silver-dark)"/>
          <stop offset="0.5" stop-color="var(--silver-light)"/>
          <stop offset="1" stop-color="var(--silver-dark)"/>
        </linearGradient>
        <linearGradient id="top-band" x1="0" y1="0" x2="1" y2="0">
          <stop offset="0" stop-color="#2a2a2a"/>
          <stop offset="0.5" stop-color="var(--band-gray)"/>
          <stop offset="1" stop-color="#4a4a4a"/>
        </linearGradient>
        <linearGradient id="ring" x1="0" y1="0" x2="1" y2="1">
          <stop offset="0" stop-color="#5a5a5a"/>
          <stop offset="0.45" stop-color="#1e1e1e"/>
          <stop offset="0.75" stop-color="#000000"/>
        </linearGradient>
      </defs>
      <path class="top-band" d="M100,0 H936 V8 C720,22 470,70 330,150 L100,150 Z" fill="url(#top-band)"/>
      <circle class="ring" cx="217" cy="244" r="152" fill="none" stroke="url(#ring)" stroke-width="34"/>
      <rect class="stripe stripe--silver" x="0" y="0" width="18" height="507" fill="url(#silver-v)"/>
      <rect class="stripe stripe--thin" x="29" y="0" width="7" height="507" fill="var(--purple)"/>
      <rect class="stripe stripe--wide" x="59" y="0" width="41" height="507" fill="var(--purple)"/>
    </svg>
    <div class="brand"><span class="brand__square"></span>Bayline Homes</div>
    <h1 class="contact__name">Dana Whitfield</h1>
    <p class="contact__title">Managing Director</p>
    <p class="contact__email">dana@baylinehomes.com</p>
    <p class="contact__phone">555.210.4837</p>
  </section>

  <section class="card card--back" aria-label="Card back">
    <svg class="card__art" viewBox="0 0 936 534" aria-hidden="true">
      <defs>
        <linearGradient id="silver-h" x1="0" y1="0" x2="1" y2="0">
          <stop offset="0" stop-color="var(--silver-dark)"/>
          <stop offset="0.3" stop-color="var(--silver-light)"/>
          <stop offset="0.6" stop-color="#b5b5b5"/>
          <stop offset="0.85" stop-color="var(--silver-light)"/>
          <stop offset="1" stop-color="var(--silver-dark)"/>
        </linearGradient>
        <linearGradient id="purple-band" x1="0" y1="0" x2="1" y2="0">
          <stop offset="0" stop-color="var(--purple)"/>
          <stop offset="0.5" stop-color="#963488"/>
          <stop offset="1" stop-color="var(--purple-deep)"/>
        </linearGradient>
      </defs>
      <rect class="band band--silver" x="0" y="430" width="936" height="19" fill="url(#silver-h)"/>
      <rect class="band band--purple" x="0" y="449" width="936" height="85" fill="url(#purple-band)"/>
    </svg>
    <div class="brand"><span class="brand__square"></span>Bayline Homes</div>
    <p class="tagline">WE BUY HOUSES FOR CASH! CALL TODAY!</p>
  </section>

</main>
</body>
</html>
```